I need a vertical business card designed to incorporate 2 Companies in wheaton IL. First company is sol e frame (I always type this with no caps and in Cataneo BT font. I like the way the L and the P surround the i) This is a Photography company that does Wedding Photography, Portraiture, Sunset, and many other types of Photography. The website is www.solframeworks.example
The other company is Grand Kiosk Max a Photo Booth rental Company. We rent photo booths to weddings and all types of events. The end project should mainly appeal to Brides and show Class. I have added 2 files One is the Grand Kiosk Max Logo and the other is on sol E frames header on the website. I do Like the eye in the sky on the sol E frame file

Target Market(s)

Future brides

Industry/Entity Type

Business

Requirements
Must have
• Grand Kiosk Max part should say A Photo Booth Rental Company
sol e frame should say All in one photography studio and address should be on this side,

```html
<!DOCTYPE html>
<html lang="en">
<head>
<meta charset="utf-8">
<title>Grand Kiosk Max – Business Card</title>
<link rel="stylesheet" href="https://fonts.googleapis.com/css2?family=Questrial&display=swap">
<style>
  :root {
    --plum-deep: #3c0634;
    --plum: #5e0a55;
    --plum-bright: #86127a;
    --band-white: #ffffff;
    --rule-grey: #a9a9a9;
    --rule-grey-dark: #7d7d7d;
    --text-grey: #a3a3a3;
    --brand-plum: #8a1a7e;
  }
  * { margin: 0; padding: 0; box-sizing: border-box; }
  html, body {
    width: 686px;
    height: 1200px;
    overflow: hidden;
    background: var(--plum-deep);
  }
  .card {
    position: relative;
    width: 686px;
    height: 1200px;
    overflow: hidden;
    font-family: "Questrial", "Helvetica Neue", Arial, sans-serif;
  }
  .silk-backdrop {
    position: absolute;
    inset: 0;
    display: block;
  }
  .logo-band {
    position: absolute;
    left: 0;
    top: 269px;
    width: 686px;
    height: 331px;
  }
  .logo-band__rule {
    position: absolute;
    left: 0;
    width: 100%;
    height: 15px;
    background: linear-gradient(to bottom, var(--rule-grey), var(--rule-grey-dark));
  }
  .logo-band__rule--top { top: 0; }
  .logo-band__rule--bottom { bottom: 0; }
  .logo-band__field {
    position: absolute;
    left: 0;
    top: 15px;
    width: 100%;
    height: 301px;
    background: var(--band-white);
    display: flex;
    align-items: center;
    justify-content: center;
  }
  .brand-name {
    font-size: 66px;
    font-weight: 400;
    color: var(--brand-plum);
    letter-spacing: 1px;
    white-space: nowrap;
  }
  .tagline {
    position: absolute;
    left: 0;
    top: 690px;
    width: 100%;
    text-align: center;
    font-size: 40px;
    line-height: 68px;
    letter-spacing: 1.5px;
    color: var(--text-grey);
    text-shadow: 2px 3px 3px rgba(0, 0, 0, 0.75);
  }
</style>
</head>
<body>
<div class="card">
  <svg class="silk-backdrop" width="686" height="1200" viewBox="0 0 686 1200" role="img" aria-label="Draped purple silk fabric backdrop">
    <defs>
      <linearGradient id="silkTone" x1="0" y1="0" x2="1" y2="1">
        <stop offset="0" stop-color="#5a0a52"/>
        <stop offset="0.35" stop-color="#6e0c64"/>
        <stop offset="0.6" stop-color="#4a0642"/>
        <stop offset="0.85" stop-color="#6a0b60"/>
        <stop offset="1" stop-color="#3e0537"/>
      </linearGradient>
      <radialGradient id="silkSheen" cx="0.7" cy="0.75" r="0.5">
        <stop offset="0" stop-color="#8a137e" stop-opacity="0.55"/>
        <stop offset="1" stop-color="#8a137e" stop-opacity="0"/>
      </radialGradient>
    </defs>
    <rect width="686" height="1200" fill="url(#silkTone)"/>
    <rect width="686" height="1200" fill="url(#silkSheen)"/>
  </svg>

  <section class="logo-band">
    <div class="logo-band__rule logo-band__rule--top"></div>
    <div class="logo-band__field">
      <span class="brand-name">Grand Kiosk Max</span>
    </div>
    <div class="logo-band__rule logo-band__rule--bottom"></div>
  </section>

  <p class="tagline">A Photo Booth<br>Rental Company</p>
</div>
</body>
</html>
```